Bref créative |
Website preferably Joomla template. | ||
Network and IT consulting. | ||
Information Technology | ||
http://quorinnetworks.com | ||
Quorin Networks has been established with the goal of becoming a recognizable brand, as a company which provides complex information technology solutions for enterprise organizations and service providers. Our services will include design and implementation of Local Area and Wide Area networks, IPv6 implementation solutions and strategies, Voice over IP, Data Center design, Server virtualization and consolidation, Wireless, and more. The initial rendition of the Quorin networks website needs to convey the technical advancement of Quorin networks, through graphics and some animation. However, the initial website will remain relatively simple in content, consisting predominantly of static content. Some flash animation may be used at a later time. To keep things simple going forward Quorin Networks would like to use Joomla to manage it’s content. A front end joomla template would be preferred but not required to ensure the site still presents a professional image. | ||
We dislike looks that are to creative and hard to distinguish. | ||
Clean/Simple Content Driven Conservative Corporate Modern Service Oriented High Tech |
Orage | ||
left side | ||
http://www.brellmarket.com/ | ||
http://www.tovanix.ca/ | ||
http://www.mireldo.com/ | ||
Please base this on our logo appearance. http://dl.hovrabin.com/u/572031/Quorin_ok.png |

```html
<!DOCTYPE html>
<html lang="en">
<head>
<meta charset="UTF-8">
<title>Quorin Networks Inc.</title>
<link rel="stylesheet" href="https://fonts.googleapis.com/css2?family=Arimo:wght@400;700&family=Oleo+Script&display=swap">
<style>
  :root {
    --amber: #f7b519;
    --amber-dark: #e29f0b;
    --ink: #1e1e1e;
    --nav: #1b1b1b;
    --slate: #474747;
    --slate-dark: #2f2f2f;
    --panel: #ffffff;
    --text: #6d6d6d;
    --heading: #222222;
    --link: #2a78b6;
    --accent-red: #c8321e;
    --social: #2f6fb4;
  }
  * { box-sizing: border-box; margin: 0; padding: 0; }
  html, body { width: 1200px; height: 1000px; overflow: hidden; }
  body {
    font-family: "Arimo", Arial, sans-serif;
    background: linear-gradient(to bottom, var(--amber) 0, var(--amber) 445px, var(--slate) 445px, var(--slate-dark) 1000px);
    position: relative;
  }
  .site { position: absolute; left: 125px; top: 0; width: 950px; height: 1000px; }

  .brand { position: absolute; left: 4px; top: 22px; display: flex; align-items: center; gap: 14px; }
  .brand-dot { width: 74px; height: 74px; border-radius: 50%; background: var(--ink); }
  .brand-name { font-size: 30px; font-weight: 700; color: var(--ink); }

  .contact-line { position: absolute; right: 0; top: 48px; font-size: 19px; font-weight: 700; color: #f4f1e6; }
  .social { position: absolute; right: 0; top: 80px; display: flex; gap: 8px; }
  .social span { width: 28px; height: 28px; border-radius: 4px; background: var(--social); display: block; }

  .main-nav {
    position: absolute; left: 0; top: 127px; width: 950px; height: 42px;
    background: linear-gradient(to bottom, #2b2b2b, var(--nav));
    display: flex; align-items: center; padding: 0 24px;
  }
  .main-nav a { text-decoration: none; font-size: 14px; font-weight: 700; color: var(--amber); margin-right: 42px; }
  .main-nav a.active { color: #fff; }
  .search { margin-left: auto; width: 260px; height: 24px; background: #fff; border-radius: 2px; display: flex; align-items: center; padding: 0 8px; font-size: 11px; color: #888; justify-content: space-between; }

  .hero { position: absolute; left: 0; top: 175px; width: 950px; height: 252px; background: linear-gradient(100deg, #0a3b68 0%, #2d7fb8 40%, #8cc3e2 70%, #e7eef2 100%); }
  .hero-strip { position: absolute; left: 0; top: 427px; width: 950px; height: 18px; background: linear-gradient(to bottom, var(--amber-dark), var(--amber)); display: flex; justify-content: center; align-items: center; gap: 9px; }
  .hero-strip i { width: 9px; height: 9px; border-radius: 50%; background: #3a3a3a; display: block; }
  .hero-strip i.on { background: #2c79b8; }

  .content { position: absolute; left: 0; top: 465px; width: 950px; height: 455px; background: var(--panel); padding: 28px 26px; }
  .content h1 { font-size: 22px; font-weight: 700; color: var(--heading); margin-bottom: 12px; }
  .intro { font-size: 11.5px; line-height: 1.5; color: var(--text); width: 890px; }
  .intro strong { color: var(--link); font-style: italic; }

  .features { position: absolute; left: 26px; top: 165px; display: flex; gap: 28px; }
  .feature { width: 186px; }
  .feature-photo { width: 186px; height: 122px; border: 1px solid #ccc; }
  .feature h3 { font-size: 13px; font-weight: 400; color: var(--link); margin: 14px 0 6px; }
  .feature p, .aside p { font-size: 11px; line-height: 1.5; color: var(--text); }
  .more { color: var(--link); font-weight: 700; }

  .aside { width: 230px; margin-left: 6px; }
  .aside h2 { font-family: "Oleo Script", cursive; font-weight: 400; font-size: 20px; color: var(--accent-red); margin-bottom: 8px; }
  .aside strong { color: var(--heading); }

  .site-footer { position: absolute; left: 0; top: 930px; width: 950px; height: 58px; background: #151515; display: flex; align-items: center; padding: 0 20px; font-size: 11px; color: #bbb; }
  .site-footer .right { margin-left: auto; display: flex; align-items: center; gap: 10px; }
  .site-footer .right b { color: var(--amber); font-weight: 400; }
  .site-footer .icons { display: flex; gap: 6px; margin-left: 6px; }
  .site-footer .icons span { width: 22px; height: 22px; border-radius: 3px; background: var(--social); display: block; }
</style>
</head>
<body>
<div class="site">
  <header>
    <div class="brand"><span class="brand-dot"></span><span class="brand-name">Quorin Networks Inc.</span></div>
    <div class="contact-line">Call Us : 5550 214 386</div>
    <div class="social"><span></span><span></span><span></span></div>
  </header>

  <nav class="main-nav">
    <a class="active" href="#">HOME</a>
    <a href="#">OUR MISSION</a>
    <a href="#">SERVICES</a>
    <a href="#">CLIENTS</a>
    <a href="#">CONTACT US</a>
    <div class="search"><span>Search entire here...</span>
      <svg width="12" height="12" viewBox="0 0 12 12"><circle cx="5" cy="5" r="3.5" fill="none" stroke="#333" stroke-width="1.6"/><line x1="7.6" y1="7.6" x2="11" y2="11" stroke="#333" stroke-width="1.8"/></svg>
    </div>
  </nav>

  <div class="hero" role="img" aria-label="Banner photo: glowing blue globe network beside a smiling business team in an office"></div>
  <div class="hero-strip"><i></i><i></i><i></i><i class="on"></i><i></i></div>

  <main class="content">
    <h1>Welcome Quorin Networks Ins.</h1>
    <p class="intro">Lorem ipsum dolor sit amet, consectetur adipisicing elit, sed do eiusmod tempor incididunt ut labore et <strong>dolore magna aliqua</strong>. Ut enim ad minim veniam, quis nostrud exercitation ullamco laboris nisi ut aliquip ex ea commodo consequat. Duis aute irure dolor in reprehenderit in voluptate velit esse cillum dolore eu fugiat nulla pariatur. Excepteur sint occaecat cupidatat non proident, sunt in culpa qui officia deserunt mollit anim id est laborum.</p>

    <div class="features">
      <div class="feature">
        <div class="feature-photo" role="img" aria-label="Photo of a dark keyboard with a blue solution key" style="background:linear-gradient(135deg,#3a3f47,#1c2026 60%,#2d6fb0)"></div>
        <h3>SOLUTION</h3>
        <p>Lorem ipsum dolor sit amet, consectetur adipisicing elit, sed do eiusmod tempor incididunt ut labore et dolore magna aliqua. Ut enim ad minim veniam. <span class="more">&#9656;</span></p>
      </div>
      <div class="feature">
        <div class="feature-photo" role="img" aria-label="Photo of a support consultant wearing a headset" style="background:linear-gradient(135deg,#e9e4dc,#c9a27a 55%,#8a5a3a)"></div>
        <h3>CONSULTING CALL</h3>
        <p>Consectetur adipisicing elit, sed do eiusmod tempor incididunt ut labore et dolore magna aliqua. Ut enim ad minim veniam. <span class="more">&#9656;</span></p>
      </div>
      <div class="feature">
        <div class="feature-photo" role="img" aria-label="Photo of a business team meeting around a laptop" style="background:linear-gradient(135deg,#f2f2f2,#b9b9b9 60%,#5a5a5a)"></div>
        <h3>DEVELOPMENT</h3>
        <p>Dolor sit amet, consectetur , sed do eiusmod tempor incididunt ut labore et dolore magna aliqua. <span class="more">&#9656;</span></p>
      </div>
      <div class="aside">
        <h2>Operations &amp; Organization</h2>
        <p><strong>Lorem ipsum</strong> dolor sit amet, consectetur adipisicing elit, sed do eiusmod tempor incididunt ut labore et <strong>dolore magna aliqua</strong>. Ut enim ad minim veniam, quis nostrud exercitation ullamco laboris nisi ut aliquip ex ea commodo consequat. Duis aute irure dolor in reprehenderit in voluptate velit esse cillum dolore eu fugiat nulla pariatur. Excepteur sint occaecat cupidatat non proident, sunt in culpa qui officia deserunt mollit anim id est laborum. <span class="more">&#9656;</span></p>
      </div>
    </div>
  </main>

  <footer class="site-footer">
    <span>Home | Our Mission | Services | Clients | Contact Us</span>
    <div class="right">
      <span>&copy; 2012 <b>QuorinNetworks.com</b>. All rights reserved</span>
      <div class="icons"><span></span><span></span><span></span></div>
    </div>
  </footer>
</div>
</body>
</html>
```